Logo + Label Design (Men’s Grooming Brand & Product Packaging)

Design a logo and 2 oz pomade label for Brant, a modern men’s grooming brand focused on clean, high-quality, natural ingredients. The design should establish a bold, masculine, minimalist identity that can later extend to products like shaving gel and body wash.

Key Requirements

Create a primary logo for “Brant” and a core label for the 2 oz pomade jar (screw-top).

Use a clean, modern style — masculine, confident, and approachable (think Wendel’s, Valto, Northfield Mill).

Design for 1–2 color screen printing on solid jar colors (white, black, or navy).

Avoid gradients, foil, or embossing. Must work in black & white.

Provide: vector logo, mockup of the 2 oz jar, color palette (CMYK/RGB/HEX), and font specs.

Winning design may lead to future projects (body wash, shave gel, skincare lines).

Font styles to use
Other font styles liked:
• We like the fonts and design concept in the attached mockup.

Requirements
Should not have
• We want to avoid too much writing or busy designs. We want to avoid having graphics/illustrations embedded in the logo if they will cause the brand to look less classy or sophisticated. We also want the design to look simple and all-American (e.g. Pellham and Stroud, Tall Pine, The BRIM, etc). We’d like to give a Kessler & Dunmore vibe that feels classy and high end.

```html
<!DOCTYPE html>
<html lang="en">
<head>
<meta charset="UTF-8">
<title>Brant Hair Pomade – 2 oz Label</title>
<link rel="stylesheet" href="https://fonts.googleapis.com/css2?family=Playfair+Display:wght@700&family=Lora:wght@400;700&display=swap">
<style>
  :root {
    --page: #f4f4f4;
    --label: #2b2c2e;
    --label-edge: #1c1d1f;
    --ink: #ffffff;
    --ink-soft: #d9d9d9;
    --accent: #5a9bd4;
  }
  * { margin: 0; padding: 0; box-sizing: border-box; }
  html, body { width: 1200px; height: 1200px; overflow: hidden; background: var(--page); }
  body { position: relative; font-family: "Lora", Georgia, serif; color: var(--ink); }

  /* Lid label */
  .lid {
    position: absolute; left: 320px; top: 90px; width: 560px; height: 560px;
    border-radius: 50%; background: var(--label);
    box-shadow: 0 0 0 14px var(--label-edge);
  }
  .lid .product-type {
    position: absolute; left: 96px; top: 280px;
    transform: translate(-50%, -50%) rotate(-90deg);
    font-size: 24px; white-space: nowrap;
  }
  .lid .divider {
    position: absolute; left: 160px; top: 130px; width: 2px; height: 300px; background: var(--ink);
  }
  .lid .info { position: absolute; left: 200px; top: 150px; }
  .wordmark {
    font-family: "Playfair Display", Georgia, serif; font-weight: 700;
    color: var(--ink); line-height: 1; letter-spacing: -1px;
  }
  .lid .wordmark { font-size: 104px; }
  .finish { font-weight: 700; font-size: 26px; line-height: 1.05; margin-top: 14px; }
  .scent { font-weight: 700; font-size: 26px; color: var(--accent); margin-top: 14px; }
  .size { font-size: 17px; letter-spacing: 1px; margin-top: 30px; }

  /* Wrap label */
  .wrap {
    position: absolute; left: 60px; top: 770px; width: 1080px; height: 330px;
    background: var(--label);
  }
  .wrap .copy {
    position: absolute; left: 30px; top: 36px; width: 330px;
    font-size: 13px; line-height: 1.45; text-align: justify; color: var(--ink-soft);
  }
  .wrap .copy p + p { margin-top: 16px; }
  .wrap .copy strong { color: var(--ink); }
  .rule { position: absolute; top: 50px; width: 2px; height: 230px; background: var(--ink); }
  .rule.one { left: 385px; }
  .rule.two { left: 700px; }
  .wrap .wordmark { position: absolute; left: 410px; top: 100px; font-size: 110px; }
  .wrap .product-type {
    position: absolute; left: 735px; top: 165px;
    transform: translate(-50%, -50%) rotate(-90deg);
    font-size: 20px; white-space: nowrap;
  }
  .wrap .info { position: absolute; left: 770px; top: 70px; }
  .wrap .finish { font-size: 22px; margin-top: 0; }
  .wrap .scent { font-size: 22px; }
  .wrap .size { font-size: 14px; margin-top: 40px; }
  .claims {
    position: absolute; left: 935px; top: 50px; width: 125px;
    border: 1px solid var(--ink-soft); padding: 12px 10px;
    font-size: 12px; line-height: 1.5; color: var(--ink-soft); list-style: none;
  }
  .claims li::before { content: "•"; margin-right: 5px; color: var(--ink); }
  .origin { position: absolute; left: 935px; top: 230px; width: 125px; font-size: 11px; color: var(--ink-soft); }
</style>
</head>
<body>

  <section class="lid" aria-label="Lid label">
    <div class="product-type">Hair Pomade</div>
    <div class="divider"></div>
    <div class="info">
      <div class="wordmark">brant</div>
      <div class="finish">Matte Finish<br>Medium Hold</div>
      <div class="scent">Fresh &amp; Clean</div>
      <div class="size">2 oz ( 57 g )</div>
    </div>
  </section>

  <section class="wrap" aria-label="Jar wrap label">
    <div class="copy">
      <p><strong>Directions:</strong> Rub small amount of pomade between hands and apply to damp hair (for sleeker look) or dry hair (for more texture). For external use only. Avoid contact with eyes. If irritation occurs, discontinue use.</p>
      <p><strong>Ingredients:</strong> Butyrospermum Parkii (Shea Butter), Cera Alba (Beeswax), Cera Bellina, Caprylic/Capric Triglyceride, Cocos Nucifera (Coconut Oil), Tocopherol (Vitamin E), Fragrance.</p>
    </div>
    <div class="rule one"></div>
    <div class="wordmark">brant</div>
    <div class="rule two"></div>
    <div class="product-type">Hair Pomade</div>
    <div class="info">
      <div class="finish">Matte Finish<br>Medium Hold</div>
      <div class="scent">Fresh &amp; Clean</div>
      <div class="size">2 oz ( 57 g )</div>
    </div>
    <ul class="claims">
      <li>Naturally derived</li>
      <li>Paraben free</li>
      <li>Alcohol free</li>
      <li>Non-greasy</li>
      <li>Water soluble</li>
    </ul>
    <div class="origin">Made in the USA</div>
  </section>

</body>
</html>
```